Business Card Design

Please copy the format of the attached card.

FRONT:
White text small blue horses head logo where "mirun" in in example

BACK:
Blue background w/ white horses head

Industry/Entity Type

Business

Contact Information for Business Card

Calvin Ostrow
Chief Executive Officer
Halvern Lodges & Resorts
412 Lindmoor Street | Alder Point, California 94109
Tel: +1.555.482.1937
email: calvin@halvernlodges.example

```html
<!DOCTYPE html>
<html lang="en">
<head>
<meta charset="utf-8">
<title>mirun business card</title>
<link rel="stylesheet" href="https://fonts.googleapis.com/css2?family=Open+Sans:wght@300;400;700&display=swap">
<style>
  :root {
    --brand-blue: #1f4f95;
    --brand-blue-dark: #153c77;
    --card-white: #f7f7f6;
    --text-grey: #6a6a6a;
    --wordmark-grey: #4a4a4a;
    --edge-grey: #8c8c8c;
    --backdrop: #e9e6e1;
  }
  * { box-sizing: border-box; margin: 0; padding: 0; }
  html, body {
    width: 1200px; height: 1023px; overflow: hidden;
    background: var(--backdrop);
    font-family: "Open Sans", Arial, sans-serif;
  }
  .sheet {
    width: 1200px; height: 1023px;
    display: flex; flex-direction: column; align-items: center; justify-content: center;
    gap: 44px;
  }
  .card {
    position: relative; width: 780px; height: 446px;
    border-radius: 4px; overflow: hidden;
    box-shadow: 0 6px 18px rgba(0,0,0,.18);
  }
  .card-front { background: var(--card-white); }
  .front-wave { position: absolute; left: 0; bottom: 0; width: 100%; height: 150px; }
  .brand-lockup { position: absolute; display: flex; align-items: center; }
  .brand-mark { border-radius: 50%; flex: none; }
  .brand-name { font-weight: 300; line-height: 1; letter-spacing: 2px; }
  .card-front .brand-lockup {
    left: 70px; top: 150px; width: 220px;
    flex-direction: column; gap: 14px;
  }
  .card-front .brand-mark { width: 60px; height: 60px; background: var(--brand-blue); }
  .card-front .brand-name { font-size: 46px; color: var(--wordmark-grey); }
  .contact {
    position: absolute; left: 330px; top: 64px;
    color: var(--text-grey); font-size: 18px; line-height: 1.34; font-weight: 300;
  }
  .contact-name { color: var(--brand-blue); font-weight: 700; font-size: 19px; }
  .contact-role { margin-bottom: 18px; }
  .contact-address { margin-bottom: 18px; }
  .contact-line { display: flex; align-items: center; gap: 10px; }
  .contact-line svg { width: 18px; height: 18px; flex: none; fill: var(--brand-blue); }
  .card-back {
    background: linear-gradient(160deg, var(--brand-blue) 0%, var(--brand-blue-dark) 100%);
  }
  .card-back .brand-lockup {
    left: 50%; top: 50%; transform: translate(-50%, -50%);
    flex-direction: row-reverse; gap: 34px;
  }
  .card-back .brand-mark { width: 110px; height: 110px; background: #ffffff; }
  .card-back .brand-name { font-size: 76px; color: #ffffff; }
</style>
</head>
<body>
<main class="sheet">
  <section class="card card-front" aria-label="Card front">
    <div class="brand-lockup">
      <span class="brand-mark"></span>
      <span class="brand-name">mirun</span>
    </div>
    <div class="contact">
      <p class="contact-name">Calvin Ostrow</p>
      <p class="contact-role">Chief Executive Officer</p>
      <p class="contact-address">412 Lindmoor Street, Alder Point<br>Westmara, 40217</p>
      <p class="contact-line">
        <svg viewBox="0 0 24 24" aria-hidden="true"><path d="M6.6 10.8a15.1 15.1 0 0 0 6.6 6.6l2.2-2.2c.3-.3.7-.4 1-.2 1.1.4 2.3.6 3.6.6.6 0 1 .4 1 1V20c0 .6-.4 1-1 1A17 17 0 0 1 3 4c0-.6.4-1 1-1h3.5c.6 0 1 .4 1 1 0 1.3.2 2.5.6 3.6.1.3 0 .7-.2 1z"/></svg>
        +1.555.482.1937
      </p>
      <p class="contact-line">
        <svg viewBox="0 0 24 24" aria-hidden="true"><path d="M2 5h20v14H2z M3.5 6.5 12 13l8.5-6.5" fill="none" stroke="#1f4f95" stroke-width="2"/></svg>
        calvin@halvernlodges.example
      </p>
    </div>
    <svg class="front-wave" viewBox="0 0 780 150" preserveAspectRatio="none" aria-hidden="true">
      <path d="M0 122 C 260 110, 470 150, 780 20 L780 150 L0 150 Z" fill="#8c8c8c"/>
      <path d="M0 128 C 260 116, 470 156, 780 30 L780 150 L0 150 Z" fill="#1f4f95"/>
    </svg>
  </section>

  <section class="card card-back" aria-label="Card back">
    <div class="brand-lockup">
      <span class="brand-mark"></span>
      <span class="brand-name">mirun</span>
    </div>
  </section>
</main>
</body>
</html>
```